Storm Restoration Contractor needs a professional business card design

Looking for a professional business card design. Not looking for your cheapo MS Word standard ones that are readily available. Dont want it to be cookie cutter look like ones readily available online. We just recently changed our logo and want to freshen up all our documents. Our company handles restoring a property back to a pre-loss condition after a storm damages it. For example, wind, hail, flood, fire losses.

Target Market(s)

Property Owners, Homeowners, Property Owners, Commercial Property Owners, Property Management Companies, Hail and Wind Damaged Properties

Industry/Entity Type

Construction Company

Contact Information for Business Card

Brightline Facades
847-555-0193
847-555-0147 fax
www.brightlinefacades.example
info@brightlinefacades.example

Requirements
Must have
• Clean, Professional, fresh look
• Storm Restoration, Roofing, Siding, Windows
Nice to have
• If there is a way to incorporate storms that may be cool.

```html
<!DOCTYPE html>
<html lang="en">
<head>
<meta charset="utf-8">
<title>Brightline Facades – Business Card</title>
<link rel="stylesheet" href="https://fonts.googleapis.com/css2?family=Playball&family=Philosopher:ital@1&display=swap">
<style>
  :root {
    --card-slate: #55565e;
    --accent-lime: #cfc83a;
    --accent-lime-deep: #b9b22e;
    --shadow-dark: #16161a;
    --ink-black: #0d0d0d;
    --text-white: #ffffff;
    --text-soft: #e4e4e8;
    --glow-light: rgba(255, 255, 255, 0.85);
  }
  html, body {
    margin: 0;
    padding: 0;
    overflow: hidden;
    background: var(--card-slate);
  }
  .business-card {
    position: relative;
    width: 1200px;
    height: 686px;
    overflow: hidden;
    background: var(--card-slate);
  }
  .accent-shape,
  .divider-rules {
    position: absolute;
    inset: 0;
  }
  .company-name {
    position: absolute;
    left: 400px;
    top: 268px;
    margin: 0;
    font-family: "Playball", cursive;
    font-weight: 400;
    font-size: 110px;
    line-height: 1;
    letter-spacing: 1px;
    color: var(--ink-black);
    white-space: nowrap;
    text-shadow:
      0 0 10px var(--glow-light),
      0 0 22px var(--glow-light),
      0 0 36px rgba(255, 255, 255, 0.5);
  }
  .contact-list {
    position: absolute;
    left: 420px;
    top: 410px;
    margin: 0;
    padding: 0;
    list-style: none;
    font-family: "Philosopher", sans-serif;
    font-style: italic;
    font-size: 38px;
    line-height: 44px;
    color: var(--text-white);
    white-space: nowrap;
  }
  .service-line {
    position: absolute;
    left: 420px;
    top: 604px;
    margin: 0;
    font-family: "Philosopher", sans-serif;
    font-style: italic;
    font-size: 28px;
    letter-spacing: 1px;
    color: var(--text-soft);
    white-space: nowrap;
  }
</style>
</head>
<body>
  <main class="business-card">
    <svg class="accent-shape" width="1200" height="686" viewBox="0 0 1200 686" aria-hidden="true">
      <defs>
        <filter id="accent-drop" x="-20%" y="-20%" width="140%" height="140%">
          <feDropShadow dx="10" dy="4" stdDeviation="9" flood-color="#16161a" flood-opacity="0.95"/>
        </filter>
      </defs>
      <ellipse cx="-40" cy="350" rx="416" ry="430" fill="var(--accent-lime)" filter="url(#accent-drop)"/>
    </svg>

    <svg class="accent-shape" width="1200" height="686" viewBox="0 0 1200 686" role="img" aria-label="Brightline Facades logo mark">
      <circle cx="170" cy="330" r="64" fill="var(--accent-lime-deep)"/>
    </svg>

    <h1 class="company-name">Brightline Facades</h1>

    <ul class="contact-list">
      <li>847-555-0193, 847-555-0147 Fax</li>
      <li>www.brightlinefacades.example</li>
      <li>info@brightlinefacades.example</li>
    </ul>

    <svg class="divider-rules" width="1200" height="686" viewBox="0 0 1200 686" aria-hidden="true">
      <rect x="326" y="551" width="854" height="5" fill="var(--text-white)"/>
      <rect x="284" y="578" width="896" height="5" fill="var(--text-white)"/>
    </svg>

    <p class="service-line">Storm Restoration · Roofing · Siding · Windows</p>
  </main>
</body>
</html>
```